External Window Signage Design - Dentist

We have 5 windows that need to have new signage designed for a Dental Clinic based in a community shopping centre.
The windows mostly line up but there is one smaller window which is lower to the ground. All 5 windows are to be covered with vinyl graphics
The windows all face the shopping centre car park under an awning.

We have attached the measurements of the window to have graphics.
We will be placing perforated once way vision vinyl as a material on the external glass. We have also attach our logo design.

We would like something simple and creative for our design. Stock images should only be used to aid in aethetics but not form the basis of the design. We prefer simple custom graphics that identifies us as a clean, modern dental clinic. We are marketing ourselves as a modern fully digital clinic where all examinations are done on a big screen which photography and 3d scanners.

Please include the words below.

Marlow Ridge Dental

Children's Dentistry
Digital Dentistry
Cosmetic Dentistry
Clearvanta
Family Dental Care
Where quality meets value - This one is our slogan, and not a service. Please use it as such.
Same Day Emergency Bookings

Please include in small text our website and phone number.
www.marlowridgedental.com.au
Phone Number TBD: 87650432

Open to different colors but our main theme is blues and greens. Similar to our logo.

Target Market(s)

20 - 40 year old dental patients. Middle Class. Some retirees as well.

Industry/Entity Type

Dental Clinic

Font styles to use
Other font styles liked:
• Comfortaa

Colors
33b8a4
34a6d7

Requirements
Must have
• Simple elegant graphics. Stock photos to aid in design if needed.
Nice to have
• Simple designs with greys, greens and blues. As per our logo.
Comfortaa font
Should not have
• Overbearing stock imagery.
Too many colors.

```html
<!DOCTYPE html>
<html lang="en">
<head>
<meta charset="utf-8">
<title>Marlow Ridge Dental – Window Signage Elevation</title>
<link href="https://fonts.googleapis.com/css2?family=Comfortaa:wght@400;600&family=Arimo&display=swap" rel="stylesheet">
<style>
  :root {
    --blue: #0f98d8;
    --blue-deep: #1a9ad6;
    --green: #82c04a;
    --frame: #000000;
    --line: #222222;
    --paper: #ffffff;
    --grey-soft: #d9d9d9;
  }
  html, body { margin: 0; padding: 0; width: 1200px; height: 644px; overflow: hidden; background: var(--paper); }
  .elevation { display: block; width: 1200px; height: 644px; }
  .brand, .service, .contact { font-family: "Comfortaa", sans-serif; }
  .dim-label { font-family: "Arimo", sans-serif; font-size: 17px; fill: var(--line); }
  .dim-line { stroke: var(--line); stroke-width: 0.8; fill: none; }
  .dim-tick { stroke: var(--line); stroke-width: 1; }
  .guide { stroke: var(--line); stroke-width: 0.7; fill: none; }
  .guide-dash { stroke: var(--line); stroke-width: 0.7; stroke-dasharray: 9 5; fill: none; }
  .frame { fill: var(--frame); }
  .glass { fill: var(--paper); }
  .band-blue { fill: var(--blue); }
  .band-green { fill: var(--green); }
  .brand-main { font-size: 22px; font-weight: 600; fill: var(--blue-deep); }
  .brand-side { font-size: 10px; font-weight: 600; fill: var(--blue-deep); }
  .brand-reverse { font-size: 10px; font-weight: 600; fill: var(--paper); }
  .service { font-size: 8px; fill: var(--blue-deep); }
  .tagline-reverse { font-size: 7px; fill: var(--paper); font-family: "Comfortaa", sans-serif; }
  .contact { font-size: 6.2px; fill: var(--paper); }
  .contact-large { font-size: 8px; fill: var(--paper); letter-spacing: 0.3px; }
  .base-box { fill: none; stroke: var(--line); stroke-width: 0.7; }
</style>
</head>
<body>
<svg class="elevation" viewBox="0 0 1200 644" xmlns="http://www.w3.org/2000/svg">
  <defs>
    <linearGradient id="hero-fill" x1="0" y1="0" x2="1" y2="1">
      <stop offset="0" stop-color="#cfd3d6"/>
      <stop offset="0.45" stop-color="#eef6fb"/>
      <stop offset="1" stop-color="#bfe6f7"/>
    </linearGradient>
  </defs>

  <!-- site guides -->
  <line class="guide-dash" x1="148" y1="72" x2="148" y2="533"/>
  <line class="guide-dash" x1="163" y1="72" x2="163" y2="533"/>
  <line class="guide-dash" x1="163" y1="477" x2="1010" y2="477"/>
  <line class="guide" x1="95" y1="533" x2="1132" y2="533"/>

  <!-- base panels -->
  <rect class="base-box" x="163" y="477" width="85" height="52"/>
  <rect class="base-box" x="315" y="477" width="156" height="52"/>
  <rect class="base-box" x="475" y="477" width="157" height="52"/>
  <rect class="base-box" x="637" y="477" width="156" height="52"/>
  <rect class="base-box" x="864" y="477" width="134" height="52"/>
  <line class="guide" x1="310" y1="475" x2="310" y2="533"/>
  <line class="guide" x1="798" y1="475" x2="798" y2="533"/>
  <line class="guide" x1="860" y1="475" x2="860" y2="533"/>
  <line class="guide" x1="1003" y1="475" x2="1003" y2="533"/>

  <!-- horizontal dimensions -->
  <g class="dimensions">
    <line class="dim-line" x1="157" y1="130" x2="253" y2="130"/>
    <line class="dim-tick" x1="157" y1="136" x2="170" y2="124"/>
    <line class="dim-tick" x1="236" y1="136" x2="249" y2="124"/>
    <line class="guide" x1="243" y1="122" x2="243" y2="163"/>
    <text class="dim-label" x="203" y="128" text-anchor="middle">605</text>

    <line class="dim-line" x1="305" y1="130" x2="802" y2="130"/>
    <line class="guide" x1="315" y1="120" x2="315" y2="163"/>
    <line class="guide" x1="471" y1="120" x2="471" y2="163"/>
    <line class="guide" x1="475" y1="120" x2="475" y2="163"/>
    <line class="guide" x1="632" y1="120" x2="632" y2="163"/>
    <line class="guide" x1="637" y1="120" x2="637" y2="163"/>
    <line class="guide" x1="793" y1="120" x2="793" y2="163"/>
    <line class="dim-tick" x1="309" y1="136" x2="321" y2="124"/>
    <line class="dim-tick" x1="465" y1="136" x2="477" y2="124"/>
    <line class="dim-tick" x1="469" y1="136" x2="481" y2="124"/>
    <line class="dim-tick" x1="626" y1="136" x2="638" y2="124"/>
    <line class="dim-tick" x1="631" y1="136" x2="643" y2="124"/>
    <line class="dim-tick" x1="787" y1="136" x2="799" y2="124"/>
    <text class="dim-label" x="393" y="128" text-anchor="middle">1,190</text>
    <text class="dim-label" x="554" y="128" text-anchor="middle">1,190</text>
    <text class="dim-label" x="715" y="128" text-anchor="middle">1,190</text>

    <line class="dim-line" x1="855" y1="130" x2="1008" y2="130"/>
    <line class="guide" x1="864" y1="120" x2="864" y2="163"/>
    <line class="guide" x1="998" y1="120" x2="998" y2="163"/>
    <line class="dim-tick" x1="858" y1="136" x2="870" y2="124"/>
    <line class="dim-tick" x1="992" y1="136" x2="1004" y2="124"/>
    <text class="dim-label" x="931" y="128" text-anchor="middle">1,020</text>
  </g>

  <!-- vertical dimensions -->
  <g class="dimensions">
    <line class="dim-line" x1="1100" y1="172" x2="1100" y2="536"/>
    <line class="guide" x1="1067" y1="180" x2="1112" y2="180"/>
    <line class="dim-tick" x1="1094" y1="174" x2="1106" y2="186"/>
    <line class="dim-tick" x1="1094" y1="523" x2="1106" y2="535"/>
    <text class="dim-label" transform="translate(1098 355) rotate(-90)" text-anchor="middle">2,660</text>

    <line class="dim-line" x1="1078" y1="216" x2="1078" y2="536"/>
    <line class="guide" x1="1044" y1="224" x2="1090" y2="224"/>
    <line class="dim-tick" x1="1072" y1="218" x2="1084" y2="230"/>
    <line class="dim-tick" x1="1072" y1="523" x2="1084" y2="535"/>
    <text class="dim-label" transform="translate(1076 375) rotate(-90)" text-anchor="middle">2,320</text>

    <line class="dim-line" x1="1055" y1="467" x2="1055" y2="542"/>
    <line class="guide" x1="1021" y1="475" x2="1066" y2="475"/>
    <line class="guide" x1="1040" y1="529" x2="1110" y2="529"/>
    <line class="dim-tick" x1="1049" y1="469" x2="1061" y2="481"/>
    <line class="dim-tick" x1="1049" y1="529" x2="1061" y2="541"/>
    <text class="dim-label" transform="translate(1052 504) rotate(-90)" text-anchor="middle">440</text>
  </g>

  <!-- low side window -->
  <g class="window window-low">
    <rect class="frame" x="88" y="219" width="161" height="256"/>
    <rect class="band-blue" x="95" y="224" width="148" height="238"/>
    <path class="band-green" d="M95,386 C125,420 190,428 243,428 L243,462 L95,462 Z"/>
    <text class="brand brand-reverse" x="169" y="330" text-anchor="middle">Marlow Ridge Dental</text>
    <text class="tagline-reverse" x="169" y="363" text-anchor="middle">Affordable Modern Dentistry</text>
    <text class="contact" x="169" y="442" text-anchor="middle">www.marlowridgedental.com.au</text>
    <text class="contact" x="169" y="453" text-anchor="middle">Phone Number 87650432</text>
  </g>

  <!-- main triple window -->
  <g class="window window-main">
    <rect class="frame" x="310" y="175" width="488" height="300"/>
    <rect class="glass" x="315" y="179" width="478" height="283"/>
    <rect role="img" aria-label="Glowing tooth illustration with orbit rings labelled with services" x="315" y="179" width="156" height="226" fill="url(#hero-fill)"/>
    <g class="plus-mark" opacity="0.18">
      <circle cx="432" cy="270" r="52" fill="none" stroke="var(--green)" stroke-width="6"/>
      <rect x="400" y="262" width="64" height="18" fill="var(--green)"/>
      <rect x="423" y="239" width="18" height="64" fill="var(--green)"/>
    </g>
    <path class="band-blue" d="M315,300 C335,350 380,380 470,370 C540,362 600,360 640,362 C700,364 760,372 793,384 L793,462 L315,462 Z"/>
    <path class="band-green" d="M315,421 C430,405 500,370 640,365 C700,364 760,372 793,384 L793,462 L315,462 Z"/>
    <text class="brand brand-main" x="638" y="275" text-anchor="middle">Marlow Ridge Dental</text>
    <text class="contact contact-large" x="553" y="449" text-anchor="middle">www.marlowridgedental.com.au</text>
    <text class="contact contact-large" x="714" y="449" text-anchor="middle">Phone Number 87650432</text>
    <rect class="frame" x="471" y="175" width="4" height="300"/>
    <rect class="frame" x="632" y="175" width="5" height="300"/>
  </g>

  <!-- right service window -->
  <g class="window window-services">
    <rect class="frame" x="860" y="175" width="143" height="300"/>
    <rect class="glass" x="864" y="179" width="134" height="283"/>
    <path class="band-green" d="M864,413 C890,428 910,431 931,431 C965,431 992,422 998,403 L998,462 L864,462 Z"/>
    <text class="brand brand-side" x="931" y="246" text-anchor="middle">Marlow Ridge Dental</text>
    <text class="service" x="931" y="274" text-anchor="middle">Affordable Modern</text>
    <text class="service" x="931" y="286" text-anchor="middle">Dentistry</text>
    <text class="service" x="931" y="309" text-anchor="middle">Digital Dentistry</text>
    <text class="service" x="931" y="332" text-anchor="middle">Cosmetic Dentistry</text>
    <text class="service" x="931" y="355" text-anchor="middle">Clearvanta</text>
    <text class="service" x="931" y="378" text-anchor="middle">Family Dental Care</text>
    <text class="service" x="931" y="401" text-anchor="middle">Where quality</text>
    <text class="service" x="931" y="413" text-anchor="middle">meets value</text>
    <text class="contact" x="931" y="442" text-anchor="middle">www.marlowridgedental.com.au</text>
    <text class="contact" x="931" y="453" text-anchor="middle">Phone Number 87650432</text>
  </g>
</svg>
</body>
</html>
```